Website images and banners needed to be created

We have a website we have not used in a few months that need updated sales banners and images resized for our web devs to upload and update. The site in question is w w w . m a r p e l y . c o m

3 page

```html
<!DOCTYPE html>
<html lang="en">
<head>
<meta charset="utf-8">
<title>The Big Black Friday Event</title>
<link href="https://fonts.googleapis.com/css2?family=Archivo:wght@800&family=Oswald:wght@700&family=Roboto:wght@400&display=swap" rel="stylesheet">
<style>
  :root {
    --bg-magenta: #9c0a5b;
    --bg-plum: #6a2a6e;
    --bg-blue: #1d4c8c;
    --text-white: #ffffff;
    --accent-yellow: #ffd400;
    --mattress-light: #e05ad2;
    --mattress-dark: #9a2a8c;
    --bed-light: #7a4a78;
    --bed-dark: #3e3a5a;
  }
  * { margin: 0; padding: 0; box-sizing: border-box; }
  html, body { width: 1200px; height: 343px; overflow: hidden; }
  .banner {
    position: relative;
    width: 1200px;
    height: 343px;
    overflow: hidden;
    background: linear-gradient(100deg, var(--bg-magenta) 0%, var(--bg-plum) 45%, var(--bg-blue) 100%);
    color: var(--text-white);
  }
  .product-mattress {
    position: absolute;
    left: 0; top: 206px;
    width: 350px; height: 115px;
    border-radius: 10px;
    background: linear-gradient(160deg, var(--mattress-light), var(--mattress-dark));
  }
  .product-bed {
    position: absolute;
    left: 667px; top: 50px;
    width: 520px; height: 259px;
    border-radius: 8px;
    background: linear-gradient(170deg, var(--bed-light), var(--bed-dark));
    opacity: 0.9;
  }
  .headline {
    position: absolute;
    left: 77px; top: 80px;
    font-family: "Archivo", Arial, sans-serif;
    font-weight: 800;
    text-transform: uppercase;
  }
  .headline__kicker { font-size: 18px; line-height: 22px; }
  .headline__rule {
    width: 76px; height: 2px;
    background: var(--text-white);
    margin: 13px 0 14px;
  }
  .headline__title { font-size: 44px; line-height: 49px; letter-spacing: 0.5px; }
  .headline__note { font-size: 15px; line-height: 20px; margin-top: 4px; }
  .headline__note-accent { color: var(--accent-yellow); }
  .offer-frame {
    position: absolute;
    left: 542px; top: 84px;
    width: 302px; height: 145px;
    border: 3px solid var(--text-white);
  }
  .offer-prefix {
    position: absolute;
    left: 559px; top: 206px;
    transform-origin: left top;
    transform: rotate(-90deg);
    font-family: "Oswald", Arial, sans-serif;
    font-weight: 700;
    font-size: 38px;
    line-height: 38px;
    letter-spacing: 1px;
    white-space: nowrap;
  }
  .offer-value {
    position: absolute;
    left: 612px; top: 80px;
    font-family: "Oswald", Arial, sans-serif;
    font-weight: 700;
    font-size: 134px;
    line-height: 160px;
    letter-spacing: -2px;
    height: 160px;
    margin-top: -22px;
  }
  .offer-percent {
    position: absolute;
    left: 756px; top: 96px;
    font-family: "Oswald", Arial, sans-serif;
    font-weight: 700;
    font-size: 72px;
    line-height: 80px;
  }
  .offer-off {
    position: absolute;
    left: 760px; top: 177px;
    font-family: "Oswald", Arial, sans-serif;
    font-weight: 700;
    font-size: 30px;
    line-height: 34px;
    letter-spacing: 2px;
  }
  .offer-scope {
    position: absolute;
    left: 540px; top: 244px;
    width: 316px;
    font-family: "Roboto", Arial, sans-serif;
    font-size: 14px;
    line-height: 18px;
    letter-spacing: 20.5px;
    white-space: nowrap;
  }
</style>
</head>
<body>
  <main class="banner">
    <div class="product-mattress" role="img" aria-label="Pink quilted mattress product photo"></div>
    <div class="product-bed" role="img" aria-label="Upholstered grey bed frame with purple bedding and pillows product photo"></div>

    <section class="headline">
      <p class="headline__kicker">The Big</p>
      <div class="headline__rule"></div>
      <h1 class="headline__title">Black Friday<br>Event</h1>
      <p class="headline__note"><span class="headline__note-accent">Sale</span> must end soon</p>
    </section>

    <div class="offer-frame"></div>
    <div class="offer-prefix">UP TO</div>
    <div class="offer-value">70</div>
    <div class="offer-percent">%</div>
    <div class="offer-off">OFF</div>
    <p class="offer-scope">EVERYTHING</p>
  </main>
</body>
</html>
```